Website Upgrade

Create new look for existing website: www.lumaverde.ca . You will find details on what we are about on the website. Email us at luma.verde@quillmail.ca if you have any questions. We will be more than happy to answer.
Luma verde is a website for women focused on empowering women.
Website must:
1. Be able to stream videos
2. Use of blogs
3. Purple must be one of the colours used in the scheme.
4. Must use existing luma verde logo (purple head with 'Luma Verde' script in white.. see on homepage). However, we are open to new logo suggestions
5. Must be professional. We are trendy but not boring.

```html
<!DOCTYPE html>
<html lang="en">
<head>
<meta charset="utf-8">
<title>Radiant Presence</title>
<link href="https://fonts.googleapis.com/css2?family=Arimo:wght@400;700&family=Roboto+Condensed:wght@700&family=Great+Vibes&display=swap" rel="stylesheet">
<style>
:root{
  --plum:#9c1470;
  --plum-ring:#b0438f;
  --plum-text:#a0166f;
  --ink:#3a3a3a;
  --body:#4a4a4a;
  --nav:#555555;
  --rule:#d4d4d4;
  --footer:#2e2e2e;
  --footer-text:#c9c9c9;
  --white:#ffffff;
}
*{box-sizing:border-box;margin:0;padding:0}
html,body{width:1200px;height:1097px;overflow:hidden;background:var(--white)}
body{position:relative;font-family:"Arimo",Arial,sans-serif;color:var(--body)}
.abs{position:absolute}

.site-header{position:absolute;left:0;top:0;width:1200px;height:94px;border-bottom:1px solid var(--rule)}
.brand{position:absolute;left:172px;top:26px;display:flex;align-items:center;gap:10px}
.brand-dot{width:28px;height:28px;border-radius:50%;background:var(--plum)}
.brand-name{font-family:"Arimo",Arial,sans-serif;font-size:21px;color:var(--plum);font-weight:400;letter-spacing:.5px}
.main-nav a{position:absolute;top:42px;font-size:13px;color:var(--nav);text-decoration:none;white-space:nowrap;transform:translateX(-50%)}

.hero{position:absolute;left:0;top:94px;width:1200px;height:444px;background:linear-gradient(180deg,#eef0ee 0%,#d9dedd 30%,#8c99a0 55%,#a9b3b6 80%,#cfd3d0 100%)}
.hero-arrow{position:absolute;top:160px}
.hero-badge{position:absolute;left:179px;top:88px;width:268px;height:268px;border-radius:50%;background:var(--plum-ring)}
.hero-badge-inner{position:absolute;left:16px;top:16px;width:236px;height:236px;border-radius:50%;background:var(--plum);color:var(--white);text-align:center}
.badge-script-lg{position:absolute;left:0;width:100%;top:42px;font-family:"Great Vibes",cursive;font-size:52px;line-height:1}
.badge-script-sm{position:absolute;left:0;width:100%;top:100px;font-family:"Great Vibes",cursive;font-size:31px;line-height:1}
.badge-rule{position:absolute;left:19px;width:198px;top:150px;height:1px;background:rgba(255,255,255,.55)}
.badge-copy{position:absolute;left:0;width:100%;top:165px;font-size:11px;line-height:19px}

.welcome-title{position:absolute;left:0;width:1200px;top:583px;text-align:center;font-family:"Roboto Condensed",sans-serif;font-weight:700;font-size:15px;color:var(--ink)}
.welcome-copy{position:absolute;left:242px;width:716px;top:620px;text-align:center;font-size:11px;line-height:21.5px;color:var(--body)}
.divider{position:absolute;left:171px;top:712px;width:858px;height:1px;background:var(--rule)}

.section-title{position:absolute;top:748px;font-family:"Roboto Condensed",sans-serif;font-weight:700;font-size:14px;color:var(--ink)}

.video{position:absolute;left:171px;top:783px;width:272px;height:175px;background:radial-gradient(circle at 55% 25%,#fbe2b8 0%,#e0a868 35%,#8a5a3a 75%,#4a3325 100%)}
.video-play{position:absolute;left:111px;top:65px;width:53px;height:37px;border-radius:7px;background:#262626}
.video-bar{position:absolute;left:3px;top:150px;width:266px;height:22px;border-radius:3px;background:rgba(30,30,30,.75)}
.video-bar-btn{position:absolute;left:0;top:0;width:38px;height:22px;border-radius:3px;background:#2b2b2b}
.video-track{position:absolute;left:48px;top:8px;width:128px;height:6px;border:1px solid #777;border-radius:3px}
.video-vol{position:absolute;left:184px;top:7px;width:20px;height:8px;background:#3aa8d8}

.post{position:absolute;top:783px;width:160px}
.post-photo{width:160px;height:150px}
.post-name{margin-top:16px;text-align:center;font-family:"Roboto Condensed",sans-serif;font-weight:700;font-size:11.5px;color:var(--plum-text)}
.post-overlay{position:absolute;left:0;top:0;width:160px;height:150px;background:rgba(40,40,40,.55)}
.post-link{position:absolute;left:65px;top:60px;width:30px;height:30px;border-radius:50%;background:rgba(255,255,255,.85)}

.site-footer{position:absolute;left:0;top:1009px;width:1200px;height:88px;background:var(--footer)}
.footer-nav a{position:absolute;top:24px;font-size:11px;color:var(--footer-text);text-decoration:none;white-space:nowrap}
.copyright{position:absolute;left:172px;top:50px;font-size:11px;color:var(--footer-text)}
.social{position:absolute;top:30px;width:29px;height:29px;border-radius:50%;border:1.5px solid #6a6a6a}
</style>
</head>
<body>

<header class="site-header">
  <div class="brand">
    <span class="brand-dot"></span>
    <span class="brand-name">The Art of Radiant Presence</span>
  </div>
  <nav class="main-nav">
    <a style="left:537px">Home</a>
    <a style="left:661px">Radiant Presence</a>
    <a style="left:782px">FAQ</a>
    <a style="left:874px">Our Bios</a>
    <a style="left:984px">Contact Us</a>
  </nav>
</header>

<section class="hero" role="img" aria-label="Photo of a woman in a white dress wading through the sea among flying seagulls">
  <svg class="hero-arrow" style="left:70px" width="20" height="90" viewBox="0 0 20 90"><polyline points="18,2 2,45 18,88" fill="none" stroke="rgba(255,255,255,.6)" stroke-width="1.2"/></svg>
  <svg class="hero-arrow" style="left:1110px" width="20" height="90" viewBox="0 0 20 90"><polyline points="2,2 18,45 2,88" fill="none" stroke="rgba(255,255,255,.6)" stroke-width="1.2"/></svg>
  <div class="hero-badge">
    <div class="hero-badge-inner">
      <div class="badge-script-lg">Be a</div>
      <div class="badge-script-sm">light for the world</div>
      <div class="badge-rule"></div>
      <p class="badge-copy">Embody your radiance, magnetism,<br>and feminine power NOW</p>
    </div>
  </div>
</section>

<h1 class="welcome-title">WELCOME TO RADIANT PRESENCE</h1>
<p class="welcome-copy">In today's world many women have unknowingly embraced masculine energy for basic survival. To get ahead in life we may compete with men by matching dominant behavior to exhibit powerful leadership, willing things to happen in order to produce results. We then carry these skills into all aspects of our personal lives.</p>
<div class="divider"></div>

<h2 class="section-title" style="left:171px">OUR VIDEOS</h2>
<div class="video" role="img" aria-label="Video still of a silhouetted woman reaching toward sunlit clouds">
  <div class="video-play">
    <svg width="53" height="37" viewBox="0 0 53 37"><polygon points="21,11 34,18.5 21,26" fill="#fff"/></svg>
  </div>
  <div class="video-bar">
    <div class="video-bar-btn"><svg width="38" height="22" viewBox="0 0 38 22"><polygon points="15,6 24,11 15,16" fill="#fff"/></svg></div>
    <div class="video-track"></div>
    <div class="video-vol"></div>
  </div>
</div>

<h2 class="section-title" style="left:496px">RECENT POSTS</h2>
<svg class="abs" style="left:1005px;top:751px" width="24" height="10" viewBox="0 0 24 10">
  <polyline points="6,1 2,5 6,9" fill="none" stroke="#999" stroke-width="1.3"/>
  <polyline points="18,1 22,5 18,9" fill="none" stroke="#999" stroke-width="1.3"/>
</svg>

<article class="post" style="left:494px">
  <div class="post-photo" role="img" aria-label="Portrait photo of author Alina Morrow" style="background:linear-gradient(160deg,#e8c29a,#d9a479 60%,#3fb391 100%)"></div>
  <div class="post-name">ALINA MORROW</div>
</article>
<article class="post" style="left:680px">
  <div class="post-photo" role="img" aria-label="Portrait photo of author Celeste Adair" style="background:linear-gradient(180deg,#7a5a8a,#5e4470 55%,#4a4448 100%)"></div>
  <div class="post-name">CELESTE ADAIR</div>
</article>
<article class="post" style="left:868px">
  <div style="position:relative">
    <div class="post-photo" role="img" aria-label="Portrait photo of author Alina Morrow" style="background:linear-gradient(160deg,#d8d4cf,#b9b6b4 50%,#5b6470 100%)"></div>
    <div class="post-overlay"></div>
    <div class="post-link">
      <svg width="30" height="30" viewBox="0 0 30 30"><g fill="none" stroke="#666" stroke-width="2" stroke-linecap="round"><path d="M13 17l4-4"/><path d="M12 14l-2 2a3 3 0 0 0 4 4l2-2"/><path d="M18 16l2-2a3 3 0 0 0-4-4l-2 2"/></g></svg>
    </div>
  </div>
  <div class="post-name">ALINA MORROW</div>
</article>

<footer class="site-footer">
  <nav class="footer-nav">
    <a style="left:172px">Home</a>
    <a style="left:248px">Radiant Presence</a>
    <a style="left:385px">FAQ</a>
    <a style="left:455px">Our BIOs</a>
    <a style="left:546px">Contact Us</a>
  </nav>
  <p class="copyright">© Copyright 2014. Radiant Presence. All Rights Reserved</p>
  <span class="social" style="left:926px"></span>
  <span class="social" style="left:962px"></span>
  <span class="social" style="left:999px"></span>
</footer>

</body>
</html>
```